Motivational Quotes Poster Series

This is a 3 poster design series for Ridgeway Haul Academy. The size of each poster should be 18 inches wide and 24 inches tall. The goal of these posters is to serve as motivational "signs" to be hung in the office area for the employees (not customers). These employees are instructors/teachers, teaching students how to drive semi trucks. While each design is a separate poster and design, we're posting as 1 project because we'd like some continuity between the series. Below we'll break down the details of all 3 posters...

Poster #1
Text that must appear on poster - "If You Want The Best Out Of Each Student" and "Give The Best Of You!" Note: While this text must appear on the poster, you can arrange in the layout as you see fit. For example, first line could be at top of poster and second line on bottom.

Poster #2
Text that must appear on poster - "Invest In People" and "Change Someone's Life" (same notes apply as in 1st poster)

Poster #3
Text that must appear on poster - "Today Is..." and "Just Another Day For You" and "The Most Important Day In Their Life" Note: This can be laid out on the poster however you see fit, but each phrase needs to be separate and it needs to flow.

Target Market(s)

Truck Driver Training Instructors - These are middle-aged, mostly male, masculine type personalities.

Industry/Entity Type

Training

Requirements
Must have
• Must have noted text from description
Must have working files (ie - PSD, EPS, AI, etc) provided
Must have common theme between each poster in series
Must have easy to read font and layout
Must have product dimensions of 18 inches (width) by 24 inches (height). If design uses full dimensions please include quarter inch bleed.
Nice to have
• Nice to have a trucking theme...related to trucking industry, but not over the top. Example - This could mean subtle injection of background tire tracks, but by no means are tire tracks required.

For inspiration, you can visit the site at http://www.ridgewayhaulacademy.com. While you can use the colors of the site/logo, you can still branch out between each poster to try new colors within reason.

Note: While we've attached the logo to this project, it COULD be used but doesn't HAVE to be included in the design. The logo IS NOT a focal point. The phrases in the poster ARE the focal point.

```html
<!DOCTYPE html>
<html lang="en">
<head>
<meta charset="utf-8">
<title>Today Is... — Ridgeway Haul Academy</title>
<link rel="stylesheet" href="https://fonts.googleapis.com/css2?family=Arimo:wght@700&display=swap">
<style>
  :root {
    --poster-green: #028f26;
    --poster-white: #ffffff;
    --tire-shade: #e9efe9;
  }
  html, body {
    margin: 0;
    padding: 0;
    width: 900px;
    height: 1200px;
    overflow: hidden;
    background: var(--poster-green);
  }
  .poster {
    position: relative;
    width: 900px;
    height: 1200px;
    background: var(--poster-green);
    font-family: "Arimo", Arial, sans-serif;
    font-weight: 700;
    color: var(--poster-white);
    overflow: hidden;
  }
  .tire-emblem {
    position: absolute;
    left: 332px;
    top: 146px;
    width: 256px;
    height: 256px;
    border-radius: 50%;
    background: radial-gradient(circle, var(--tire-shade) 0%, var(--poster-white) 70%);
  }
  .phrase {
    position: absolute;
    left: 0;
    width: 900px;
    margin: 0;
    text-align: center;
    font-size: 80px;
    line-height: 100px;
    font-weight: 700;
    letter-spacing: 0.5px;
  }
  .phrase-opening { top: 423px; left: 5px; }
  .phrase-routine { top: 573px; left: -10px; }
  .phrase-impact  { top: 833px; }
  .academy-name {
    position: absolute;
    left: 0;
    width: 900px;
    top: 1140px;
    text-align: center;
    font-size: 26px;
    line-height: 40px;
    font-weight: 700;
    color: var(--poster-white);
    letter-spacing: 0.5px;
  }
</style>
</head>
<body>
  <main class="poster">
    <div class="tire-emblem" role="img" aria-label="White truck tire and wheel illustration"></div>

    <p class="phrase phrase-opening">Today Is...</p>
    <p class="phrase phrase-routine">Just Another Day<br>For You</p>
    <p class="phrase phrase-impact">The Most Important<br>Day In Their Life</p>

    <div class="academy-name">Ridgeway Haul Academy</div>
  </main>
</body>
</html>
```